need eczema bath soak label/bag

need you to recreate this please. ai file. recreate this exact image please. ...if you want a big tip, create some different styles.

Colors
0054AA
0677BA
7BADD7
CADEEF
E8F1F8

```html
<!DOCTYPE html>
<html lang="en">
<head>
<meta charset="utf-8">
<title>Eczema Bath Soak – Pouch Label</title>
<link rel="stylesheet" href="https://fonts.googleapis.com/css2?family=Dancing+Script:wght@500&family=Montserrat:wght@400;700&display=swap">
<style>
  :root {
    --backdrop: #ecebe6;
    --pouch-white: #f7f8f6;
    --seal-line: #e3e5e2;
    --script-teal: #4f9383;
    --sand-tan: #c9a887;
    --deep-teal: #0b4a52;
    --sea-teal: #1c9e93;
    --sea-light: #8fd3c8;
    --foam: #f4f7f5;
    --sand-light: #dcc3a3;
    --sand-mid: #d2b58f;
    --sand-dark: #c6a47c;
    --badge-line: rgba(255, 255, 255, 0.85);
  }
  * { margin: 0; padding: 0; box-sizing: border-box; }
  html, body {
    width: 1200px;
    height: 1200px;
    overflow: hidden;
    background: var(--backdrop);
  }
  .canvas {
    position: relative;
    width: 1200px;
    height: 1200px;
  }
  .label {
    position: absolute;
    left: 210px;
    top: 80px;
    width: 780px;
    height: 1040px;
    background: var(--pouch-white);
    overflow: hidden;
  }
  .label__seal {
    position: absolute;
    left: 0;
    right: 0;
    height: 2px;
    background: var(--seal-line);
  }
  .label__seal--upper { top: 38px; }
  .label__seal--lower { top: 52px; }
  .label__sea {
    position: absolute;
    left: 0;
    right: 0;
    top: 225px;
    height: 390px;
    background: linear-gradient(180deg,
      rgba(247, 248, 246, 0) 0%,
      var(--sea-light) 10%,
      var(--sea-teal) 24%,
      var(--foam) 40%,
      var(--sea-teal) 52%,
      var(--sea-light) 62%,
      var(--foam) 78%,
      var(--foam) 92%,
      var(--sand-light) 100%);
  }
  .label__sand {
    position: absolute;
    left: 0;
    right: 0;
    top: 612px;
    bottom: 0;
    background: linear-gradient(180deg, var(--sand-light) 0%, var(--sand-mid) 45%, var(--sand-dark) 100%);
  }
  .label__tagline {
    position: absolute;
    top: 88px;
    left: 0;
    right: 0;
    text-align: center;
    font-family: "Dancing Script", cursive;
    font-weight: 500;
    font-size: 38px;
    color: var(--script-teal);
    letter-spacing: 1px;
  }
  .label__title {
    position: absolute;
    top: 228px;
    left: 0;
    right: 0;
    text-align: center;
    font-family: "Montserrat", sans-serif;
  }
  .label__condition {
    display: block;
    font-weight: 400;
    font-size: 62px;
    letter-spacing: 7px;
    color: var(--sand-tan);
    line-height: 1;
    margin-bottom: 16px;
  }
  .label__product {
    display: block;
    font-weight: 700;
    font-size: 112px;
    letter-spacing: 9px;
    color: var(--deep-teal);
    line-height: 1.06;
  }
  .label__badge {
    position: absolute;
    left: 288px;
    top: 762px;
    width: 200px;
    height: 200px;
  }
</style>
</head>
<body>
<main class="canvas">
  <section class="label">
    <div class="label__seal label__seal--upper"></div>
    <div class="label__seal label__seal--lower"></div>
    <div class="label__sea" role="img" aria-label="Photograph of a turquoise ocean wave with white foam washing onto the shore"></div>
    <div class="label__sand" role="img" aria-label="Photograph of fine golden beach sand"></div>
    <p class="label__tagline">herbal product</p>
    <h1 class="label__title">
      <span class="label__condition">ECZEMA</span>
      <span class="label__product">BATH</span>
      <span class="label__product">SOAK</span>
    </h1>
    <svg class="label__badge" viewBox="0 0 200 200" aria-hidden="true">
      <circle cx="100" cy="100" r="94" fill="none" stroke="var(--badge-line)" stroke-width="4"/>
    </svg>
  </section>
</main>
</body>
</html>
```